Custom Header Designs - Automotive Parts - Alternator & Starter

We need 8 Header/Hero designs that will be used on our website. We are a company based in Montreal Canada and we re-manufacture Alternators and Starters for all types of vehicles. We offer a premium product and we are looking for premium designs that reflect the look of our packaging and the look of our website. Essentially we specialize in the sale and manufacture of two specific parts that go on all types of vehicles, Alternators and Starters. All text on these designs need to be editable as we will need to translate them to French once we get the source files.
Here are some websites of our competitors so you can draw some inspiration and see what our industry/business is all about:
https://www.quellorn.com/
https://www.rivetanvil.com/
Article that describes a remanufactured product, https://www.zephtrove.com/articles/starters-and-alternators-reman-vs-new.html
Our packaging is modern, sleek and professional. Our website is a B2B E-Commerce Site as well as an info site to promote our products. It is clean and minimal but we want the header/hero designs to help it stand out. Our main colors are blue and gray (as seen in our logo), but you can use whatever you like to compliment these colors.
Our packaging design was done on PixelHarbor, here is the link to that project so that you can see the packaging look and use any of the info that is from that project.
https://jobs.pixelharbor.ca/job/5820467
The 8 Header/Hero designs will be used in the following areas, I have included a brief description of what we are looking for:
1 - Homepage Header/Hero image - This will be the homepage hero image therefore it should summarize the info described below. We offer premium quality re-manufactured alternators and starters. We are a wholesaler/distributor that services major auto-part stores with these quality products.
2 - General Product Header/Hero image - This image will be used as a header where the customer can learn general info about our products and any custom work we can do. This page will have a section where you can click to learn more about our individual product lines (links to product specific pages mentioned below) and a description of the custom work we can perform. We offer a two year manufacturers warranty.
3 - Alternator Product Header/Hero image - This image will be used to showcase our Alternator Product Line. Its purpose is to promote and advertise our premium re-manufactured alternators. This page will provide detailed info about our alternator re-manufacturing process and describe why our alternators are great.
4 - Starter Product Header/Hero image - This image will be used to showcase our Starter Product Line. Its purpose is to promote and advertise our premium re-manufactured starters. This page will provide detailed info about our starter re-manufacturing process and describe why our starters are great.
5 - General Header/Hero Image - This image will be used in most of our standard pages like our terms and conditions, privacy policy, warranty policy, our company page, etc. It needs to relate to the industry but be general enough so that we could use it in multiple areas
6 - Online Ordering Header image - This image will be used in our B2B area to introduce our customers to the Online Ordering system, its purpose is to advertise and explain some of the features of the Online Ordering system.
7 - B/O Re-Manufacture & Return Header Image - This image will be used in our B2B area to explain and advertise to our customers how our Backorder/R&R process works on our website. Essentially if we do not have the remanufactured part in stock but we have the core you could put the product on Backorder and we will remanufacture it in a few hours. If for any reason (rare vehicle, old vehicle, etc.) we do not have the core we will R&R (Remanufacture and Return) the customers core for them.
8 - Bulk Ordering Form Header Image - This image will be used in our B2B area to explain and advertise to our customers how our Bulk Ordering Form works on our website.
These hero/header images will be going on a Wordpress/WooCommerce website and I am suggesting these images have a size of 1600 x 500, but we will take any other suggestions from the designers as you are the experts.
I have included a zip file that includes images of various elements that will help you in the design process.
Target Market(s)
Educate consumers about our products and attract auto supply chains to become distributors of our products.
Industry/Entity Type
Automotive Part

```html
<!DOCTYPE html>
<html lang="en">
<head>
<meta charset="utf-8">
<title>Alternator</title>
<link rel="stylesheet" href="https://fonts.googleapis.com/css2?family=Big+Shoulders+Display:wght@900&family=Cabin:wght@700&display=swap">
<style>
  :root {
    --navy: #15216b;
    --band-deep: #121d63;
    --band-bright: #2337b8;
    --text-blue: #1a2a9c;
    --white: #ffffff;
    --rule-dark: #5e5e66;
    --rule-light: #d8d8dc;
    --floor: #e4e4e8;
    --metal-light: #e9ebee;
    --metal-mid: #b9bdc4;
    --metal-dark: #6d727b;
  }
  html, body {
    margin: 0;
    padding: 0;
    overflow: hidden;
  }
  .hero {
    position: relative;
    width: 1200px;
    height: 467px;
    overflow: hidden;
    background: linear-gradient(to bottom, var(--white) 0%, var(--white) 82%, var(--floor) 100%);
  }
  .title-band {
    position: absolute;
    left: 0;
    top: 104px;
    width: 1180px;
    height: 164px;
    background:
      radial-gradient(ellipse 420px 160px at 780px 90px, rgba(60, 90, 230, 0.55), transparent 70%),
      linear-gradient(to right, var(--band-deep) 0%, var(--band-deep) 45%, var(--band-bright) 80%, var(--band-deep) 100%);
  }
  .band-rule {
    position: absolute;
    left: 0;
    top: 268px;
    width: 1180px;
    height: 9px;
    background: linear-gradient(to right, var(--rule-dark) 0%, #9a9aa2 40%, var(--rule-light) 80%, var(--white) 100%);
  }
  .title {
    position: absolute;
    left: 44px;
    top: 118px;
    margin: 0;
    font-family: "Big Shoulders Display", "Arial Narrow", sans-serif;
    font-weight: 900;
    font-size: 134px;
    line-height: 1;
    letter-spacing: 1px;
    color: var(--white);
  }
  .intro {
    position: absolute;
    left: 45px;
    top: 292px;
    width: 660px;
    margin: 0;
    font-family: "Cabin", "Trebuchet MS", sans-serif;
    font-weight: 700;
    font-size: 20.4px;
    line-height: 26.6px;
    color: var(--text-blue);
  }
  .product-visual {
    position: absolute;
    left: 719px;
    top: 30px;
    width: 462px;
    height: 405px;
    border-radius: 46% 40% 38% 44%;
    background:
      radial-gradient(circle at 30% 57%, var(--metal-dark) 0 12%, var(--metal-light) 13% 22%, transparent 23%),
      radial-gradient(ellipse at 55% 45%, var(--metal-light) 0%, var(--metal-mid) 55%, var(--metal-dark) 100%);
  }
</style>
</head>
<body>
  <div class="hero">
    <div class="title-band"></div>
    <div class="band-rule"></div>
    <h1 class="title">ALTERNATOR</h1>
    <p class="intro">The alternator charges the battery and keeps the electrical accessories of the car working while it is running. When the alternator loses capacity or fails, the electrical systems will only stay on until the battery's reserve charge is depleted. Your car might die, but you may be able to restart it with a jump start.</p>
    <div class="product-visual" role="img" aria-label="Chrome remanufactured alternator with ribbed pulley, shown at an angle"></div>
  </div>
</body>
</html>
```